Timber Ridge Land Services Business Cards

Need to create a business card with the company logo "Timber Ridge Land Services". The business will provide forestry mulching for land clearing and vegetation control, brush and small tree removal, wildlife habitat improvement and trail and property access creation.

```html
<!DOCTYPE html>
<html lang="en">
<head>
<meta charset="utf-8">
<title>Timber Ridge Land Services – Business Cards</title>
<link rel="stylesheet" href="https://fonts.googleapis.com/css2?family=Montserrat:wght@400;500;700;800&display=swap">
<style>
  :root {
    --backdrop: #2e2e2e;
    --ink-black: #151515;
    --forest: #005a46;
    --leaf: #6cc16d;
    --paper: #ffffff;
    --teal-card: #005e4c;
    --teal-mark: #2f9d83;
    --text-light: #f2f2f2;
  }
  * { margin: 0; padding: 0; box-sizing: border-box; }
  html, body {
    width: 1200px; height: 780px; overflow: hidden;
    background: var(--backdrop);
    font-family: "Montserrat", Arial, sans-serif;
  }
  .sheet {
    position: relative; width: 1200px; height: 780px;
    display: flex; align-items: center; justify-content: center; gap: 50px;
  }
  .card {
    position: relative; width: 540px; height: 310px; overflow: hidden;
    box-shadow: 0 14px 30px rgba(0,0,0,.45);
  }
  .card-front { background: var(--paper); }
  .front-waves { position: absolute; inset: 0; width: 100%; height: 100%; }

  .contact { position: absolute; left: 26px; top: 30px; color: var(--text-light); }
  .contact-name {
    color: var(--leaf); font-weight: 800; font-size: 17px;
    letter-spacing: .3px; text-transform: uppercase; white-space: nowrap;
  }
  .contact-role { font-size: 12px; margin-top: 2px; }
  .contact-address { font-size: 12px; margin-top: 12px; line-height: 1.35; }
  .contact-list { list-style: none; margin-top: 10px; font-size: 12px; }
  .contact-list li { display: flex; align-items: center; gap: 7px; margin-bottom: 4px; }
  .contact-icon { width: 11px; height: 11px; flex: none; }

  .follow { position: absolute; left: 150px; bottom: 20px; display: flex; align-items: center; gap: 12px; }
  .follow-label { color: var(--leaf); font-size: 20px; font-weight: 500; white-space: nowrap; }
  .social-dots { display: flex; gap: 6px; }
  .social-dot { width: 16px; height: 16px; border-radius: 50%; background: var(--leaf); }

  .brand-name {
    color: var(--forest); font-weight: 800; text-transform: uppercase;
  }
  .card-front .brand-name {
    position: absolute; right: 26px; top: 62px; text-align: left;
  }
  .card-front .brand-text { font-size: 20px; line-height: 1.1; display: block; white-space: nowrap; }

  .card-back {
    background: var(--teal-card);
    display: flex; align-items: center; justify-content: center;
  }
  .card-back .brand-name { display: flex; align-items: center; gap: 12px; color: var(--teal-mark); }
  .card-back .brand-text { font-size: 32px; line-height: 1.05; letter-spacing: .5px; }
  .brand-dot { width: 22px; height: 22px; border-radius: 50%; background: var(--teal-mark); flex: none; }
</style>
</head>
<body>
<main class="sheet">
  <section class="card card-front">
    <svg class="front-waves" viewBox="0 0 540 310" preserveAspectRatio="none" aria-hidden="true">
      <path d="M0 0 H245 C320 60 280 230 430 310 H0 Z" fill="var(--forest)"/>
      <path d="M0 0 H233 C308 60 268 230 418 310 H0 Z" fill="var(--leaf)"/>
      <path d="M0 0 H221 C296 60 256 230 406 310 H0 Z" fill="var(--paper)"/>
      <path d="M0 0 H215 C290 60 250 230 400 310 H0 Z" fill="var(--ink-black)"/>
    </svg>

    <div class="contact">
      <p class="contact-name">Dana Whitfield</p>
      <p class="contact-role">Managing Director</p>
      <p class="contact-address">Your address, City<br>State, Zip 1234</p>
      <ul class="contact-list">
        <li><svg class="contact-icon" viewBox="0 0 12 12"><path d="M3 1 L5 3.5 L4 5 C5 7 6 8 7 8.5 L8.5 7.5 L11 9.5 L9.5 11 C5 10.5 1.5 7 1 2.5 Z" fill="var(--leaf)"/></svg>123 456 789</li>
        <li><svg class="contact-icon" viewBox="0 0 12 12"><rect x="1" y="2.5" width="10" height="7" fill="none" stroke="var(--leaf)" stroke-width="1.4"/><path d="M1 3 L6 7 L11 3" fill="none" stroke="var(--leaf)" stroke-width="1.2"/></svg>info@timberridgeland.com</li>
        <li><svg class="contact-icon" viewBox="0 0 12 12"><circle cx="6" cy="6" r="5" fill="none" stroke="var(--leaf)" stroke-width="1.4"/><path d="M1 6 H11 M6 1 C3.5 4 3.5 8 6 11 C8.5 8 8.5 4 6 1" fill="none" stroke="var(--leaf)" stroke-width="1"/></svg>www.timberridgeland.com</li>
      </ul>
    </div>

    <div class="follow">
      <span class="follow-label">Follow Us</span>
      <span class="social-dots">
        <span class="social-dot" role="img" aria-label="Social profile link"></span>
        <span class="social-dot" role="img" aria-label="Social profile link"></span>
        <span class="social-dot" role="img" aria-label="Social profile link"></span>
      </span>
    </div>

    <div class="brand-name">
      <span class="brand-text">Timber Ridge</span>
      <span class="brand-text">Land Services</span>
    </div>
  </section>

  <section class="card card-back">
    <div class="brand-name">
      <span class="brand-dot"></span>
      <span class="brand-text">Timber Ridge<br>Land Services</span>
    </div>
  </section>
</main>
</body>
</html>
```